financial company web page

We are tax and financial consulting company that needs a web site. Our logo is attached. Headquarters of our company is based in Latvia, Riga. Our actual temporary web site is www.corvanteq.com The main purpose of our new web site is:
* to explain the benefits of doing business through Latvian LLC companies;
* provide necessary information about taxation regime in Latvia for trading and holding companies
* propose some standard schemes of using Latvian companies for various businesses.
* offer our clients other jurisdictions companies - other European, offshore, etc.
* offer our clients ecommerce solutions
* offer our client residency in Latvia and EU
Registration of a Latvian company + accounting + legal advice will be our primary product. However, web site first page should highlight 4 other important products, such as:
1 - eCommerce (here we will explain briefly what is eCommerce, how our client can use it, what are the bonuses doing business online, explain conditions of eCommerce, etc) ;
2 - Residence Permit (here we offer EU and non-EU citizens to obtain Latvian residence permit and explain the benefits of having Latvian ID card);
3 - other Jurisdictions (here we propose list of other companies registered in the countries with favorable taxation regime, i.e. UK, Hong-Kong, Canada, Panama, BVI, UAE, etc);
4 - banking (here we explain benefits of having bank account in Latvia, explaining briefly products that bank offer, etc).
Overall Website map is the following:
1. About us
2. About Latvia
3. Contacts
4. Latvian company
5. Our services
a. еCommerce
b. Resident permit (Latvia and EU)
c. Bank accounts
d. Registration and support of other jurisdictions (European companies, Low tax companies, Offshore companies)
e. Additional services (Tax advisory, Virtual office, European licenses, Accounting services, Legal address in Riga)
6. Become Partner
7. Corvanteq Travel Guide
As a start point we need only first page design. If this design suits us well we will continue to work with you on other pages. We are looking for innovative, creative and professional design in line with our corporate logo and colours. We want this design to focus more on graphic, on simplicity and usability. It should be immediately clear from the first glance what the site is about, what is our key product and how to get more information if I'm interested on something.
These are website from our sector, we want to be better:
http://www.marlowbayholdings.com/
http://www.qtr-harbourline.com/
http://www.dwpenterprisehub.com/
http://www.firmsetupnorth59.co.uk/
In case you can't find our logo, please, ask I will send it to your mail. Thanks!
Target Market(s)
European, Russian or Chinesee enterpreneurs
Industry/Entity Type
Accounting
Requirements
Must have
- Web site will be on 10 languages, so somewhere must be a button/flag to switch language.
Contact information should be on every page (phone number and add Chatterloop buttons or similar).
Search button should be available on the first page
Button Request a Call should be on every page.
Visitors should also have a possibility to download a brochure about each product (so appropriate button should be in each section).

```html
<!DOCTYPE html>
<html lang="en">
<head>
<meta charset="utf-8">
<title>Corvanteq — Tax and Financial Solutions</title>
<link rel="stylesheet" href="https://fonts.googleapis.com/css2?family=Source+Sans+3:wght@400;600;700&family=PT+Sans+Narrow:wght@400;700&display=swap">
<style>
:root{
  --navy:#0d4a8a;
  --navy-dark:#083a70;
  --blue:#1a5ea8;
  --sky:#3aa7d6;
  --sky-dark:#1f86b8;
  --text:#6b6b6b;
  --text-dark:#444;
  --grey-bg:#ececec;
  --line:#dcdcdc;
  --white:#fff;
}
*{margin:0;padding:0;box-sizing:border-box}
html,body{width:1200px;height:988px;overflow:hidden;background:var(--white)}
body{font-family:"Source Sans 3",sans-serif;color:var(--text)}
.page{position:relative;width:1400px;height:1153px;transform:scale(.857143);transform-origin:0 0}
.abs{position:absolute}
.narrow{font-family:"PT Sans Narrow",sans-serif}

/* header */
.brand{left:210px;top:26px;display:flex;align-items:center;gap:12px}
.brand-mark{width:58px;height:58px;border-radius:50%;background:var(--navy)}
.brand-name{font-size:40px;font-weight:700;color:var(--navy);line-height:1}
.brand-tag{font-size:9.5px;letter-spacing:.6px;color:#888;margin-top:2px}
.lang-label{left:564px;top:58px;font-size:12px;color:#666}
.lang-select{left:660px;top:52px;width:99px;height:25px;border:1px solid #cfcfcf;border-radius:3px;background:linear-gradient(#fff,#eee);font-size:12px;color:#444;display:flex;align-items:center;padding-left:8px;gap:8px}
.lang-flag{width:20px;height:13px;background:#2b3f7a;border:1px solid #b22}
.lang-caret{margin-left:auto;margin-right:7px;border:4px solid transparent;border-top-color:#555;margin-top:4px}
.search{left:772px;top:53px;width:177px;height:25px;border:1px solid #cfcfcf;border-radius:2px;font-size:12px;color:#aaa;padding:5px 8px}
.search svg{position:absolute;right:8px;top:6px}
.chat{left:1000px;top:28px;width:189px;height:56px;border-radius:5px;background:linear-gradient(#8a8a8a,#3a3a3a);color:#fff;padding:9px 0 0 59px}
.chat small{display:block;font-size:12px;font-weight:600}
.chat b{font-size:17px;font-weight:600}
.chat-dot{left:983px;top:22px;width:64px;height:64px;border-radius:50%;background:radial-gradient(circle at 40% 35%,#6fd0ff,#139ee0);border:3px solid #fff}

/* navigation */
.nav{left:210px;top:108px;width:980px;height:41px;border-radius:3px;background:linear-gradient(#1456a0,var(--navy-dark));display:flex;justify-content:space-around;align-items:center}
.nav a{font-family:"PT Sans Narrow",sans-serif;color:#fff;text-decoration:none;font-size:13.5px}
.submenu{left:641px;top:150px;width:149px;height:139px;background:rgba(27,88,160,.92);border-radius:3px;padding:9px 0 0 20px;z-index:3}
.submenu a{display:block;font-family:"PT Sans Narrow",sans-serif;color:#fff;font-size:11px;text-decoration:none;line-height:25px}

/* partner promo */
.partner{left:210px;top:162px;width:234px;height:221px;background:linear-gradient(var(--blue),var(--navy-dark));border-radius:3px;overflow:hidden}
.partner-photo{right:0;top:8px;width:112px;height:213px;background:linear-gradient(#e7e9ee,#c9ccd4);border-radius:50px 0 0 0}
.partner-text{left:18px;top:32px;color:#fff;font-family:"PT Sans Narrow",sans-serif}
.partner-text .t1{font-size:17px}
.partner-text .t2{font-size:28px;color:#5fd1ff;line-height:1}
.partner-text p{font-size:11.5px;line-height:19px;margin-top:8px;width:110px}
.btn-sky{background:linear-gradient(#5cc0e8,var(--sky-dark));color:#10466f;font-family:"PT Sans Narrow",sans-serif;font-size:12px;border-radius:2px;display:flex;align-items:center;justify-content:center}
.partner .btn-sky{position:absolute;left:18px;top:176px;width:88px;height:26px}

/* brochure */
.brochure{left:210px;top:395px;width:234px;height:68px;border-radius:3px;background:linear-gradient(#b5b5b5,#6f6f6f);color:#fff;font-family:"PT Sans Narrow",sans-serif;font-size:16px;line-height:21px;padding:12px 0 0 71px}
.brochure-icon{left:10px;top:9px;width:48px;height:48px;border-radius:4px;background:linear-gradient(#fff,#ddd)}

/* hero */
.hero{left:465px;top:162px;width:725px;height:301px;background:linear-gradient(90deg,#6d8fbd 0%,#275a9b 45%,#0e4585 100%);overflow:hidden}
.hero-photo{left:0;top:0;width:440px;height:301px;background:linear-gradient(160deg,#a8bfdc,#4c74ad 60%,#2d5790)}
.hero-copy{left:459px;top:96px;color:#fff;font-family:"PT Sans Narrow",sans-serif}
.hero-copy h2{font-weight:400;font-size:36px;line-height:1}
.hero-copy p{font-size:14px;line-height:25px;margin-top:8px;width:250px}
.hero-dots{right:12px;bottom:12px;display:flex;gap:3px}
.hero-dots i{width:9px;height:9px;background:rgba(255,255,255,.45)}
.hero-dots i:first-child{background:#fff}

/* request call */
.callband{left:465px;top:469px;width:725px;height:107px;background:linear-gradient(#e6e6e6,#fff 60%);border-bottom:1px solid var(--line)}
.callband h3{position:absolute;right:199px;top:20px;font-family:"PT Sans Narrow",sans-serif;font-weight:400;font-size:17px;color:var(--navy)}
.callband p{position:absolute;right:199px;top:48px;width:520px;text-align:right;font-family:"PT Sans Narrow",sans-serif;font-size:10.5px;line-height:18px;color:#555}
.call-btn{right:16px;top:19px;width:163px;height:58px;border-radius:4px;background:linear-gradient(#4ba7e0,#1566b0);border:1px solid #0f5493;color:#fff;font-size:20px;font-style:italic;font-weight:600;display:flex;align-items:center;justify-content:center}

/* sidebar services */
.side-title{font-family:"PT Sans Narrow",sans-serif;font-size:17px;color:var(--navy)}
.svc-list{left:210px;top:519px;width:234px}
.svc-list a{display:flex;align-items:center;height:32px;margin-bottom:8px;padding-left:14px;font-family:"PT Sans Narrow",sans-serif;font-size:11.5px;color:#777;text-decoration:none;background:linear-gradient(#fff,#ededed)}
.svc-list a::before{content:"›";margin-right:6px;font-size:14px}
.svc-list a.active{background:linear-gradient(#57bde6,var(--sky-dark));color:#0d4268}
.city-photo{left:210px;top:773px;width:234px;height:127px;background:linear-gradient(#dce6ef,#8c9aa8 60%,#6a6f78)}
.side-copy{left:210px;top:914px;width:230px;font-size:11px;line-height:18px}

/* about */
.about-title{left:466px;top:597px}
.about-copy{left:469px;top:624px;width:722px;font-size:11px;line-height:18px}
.about-copy p+p{margin-top:18px}

/* feature columns */
.feature-head{top:775px;height:35px;background:linear-gradient(#f4f4f4,#dedede);font-family:"PT Sans Narrow",sans-serif;font-size:14.5px;color:var(--navy);padding:9px 0 0 16px}
.feature-copy{top:826px;width:352px;font-size:11px;line-height:18px}
.feature-list{top:898px;display:grid;grid-template-columns:177px 180px;row-gap:0}
.feature-list span{display:flex;align-items:center;gap:14px;height:29px;font-family:"PT Sans Narrow",sans-serif;font-size:11.5px;color:#333}
.feature-list svg{flex:none}
.feature-btn{top:995px;width:112px;height:27px}

/* footer */
.footer{left:210px;top:1053px;width:980px;height:72px;background:linear-gradient(#ececec,#fff)}
.footer-links{position:absolute;left:28px;top:22px;font-size:11px;color:#666;display:flex;gap:15px}
.footer-links i{font-style:normal;color:#999}
.footer-copy{position:absolute;left:28px;top:43px;font-size:11px;color:#666}
.social{position:absolute;right:17px;top:29px;display:flex;gap:4px}
.social i{width:24px;height:24px;border-radius:50%;background:#9a9a9a}
</style>
</head>
<body>
<div class="page">

  <header>
    <div class="abs brand">
      <div class="brand-mark"></div>
      <div>
        <div class="brand-name">Corvanteq</div>
        <div class="brand-tag">TAX AND FINANCIAL SOLUTIONS</div>
      </div>
    </div>
    <div class="abs lang-label">Select Language :</div>
    <div class="abs lang-select"><span class="lang-flag"></span>English<span class="lang-caret"></span></div>
    <div class="abs search">Search
      <svg width="12" height="12" viewBox="0 0 12 12"><circle cx="5" cy="5" r="3.5" fill="none" stroke="#bbb" stroke-width="1.4"/><path d="M7.5 7.5 11 11" stroke="#bbb" stroke-width="1.6"/></svg>
    </div>
    <div class="abs chat"><small>Live Chat</small><b>corvanteq@info</b></div>
    <div class="abs chat-dot" aria-label="Chatterloop"></div>
  </header>

  <nav class="abs nav">
    <a href="#">ABOUT US</a><a href="#">ABOUT LATVIA</a><a href="#">LATVIAN COMPANY</a><a href="#">OUR SERVICES</a><a href="#">BECOME PARTNER</a><a href="#">CORVANTEQ TRAVEL GUIDE</a><a href="#">CONTACTS</a>
  </nav>
  <div class="abs submenu">
    <a href="#">ECOMMERCE</a><a href="#">RESIDENT PERMIT</a><a href="#">BANK ACCOUNTS</a><a href="#">REGISTRATION</a><a href="#">ADDITIONAL SERVICES</a>
  </div>

  <aside>
    <div class="abs partner">
      <div class="abs partner-photo" role="img" aria-label="Smiling businesswoman pointing forward"></div>
      <div class="abs partner-text">
        <div class="t1">BECOME A</div>
        <div class="t2">PARTNER</div>
        <p>CORVANTEQ IS A TAX ADVISORY FIRM ESTABLISHED BACK IN 2002 IN LIMASSOL,</p>
      </div>
      <div class="btn-sky">CLICK HERE</div>
    </div>
    <div class="abs brochure">
      <div class="abs brochure-icon"></div>
      OUR<br>BROCHURE DOWNLOAD
    </div>

    <h3 class="abs side-title" style="left:211px;top:487px">SERVICES</h3>
    <div class="abs svc-list">
      <a class="active" href="#">ECOMMERCE</a>
      <a href="#">RESIDENT PERMIT</a>
      <a href="#">BANK ACCOUNTS</a>
      <a href="#">REGISTRATION</a>
      <a href="#">ADDITIONAL SERVICES</a>
    </div>

    <h3 class="abs side-title" style="left:211px;top:737px">LATVIAN COMPANY</h3>
    <div class="abs city-photo" role="img" aria-label="Wide-angle view of modern office towers"></div>
    <p class="abs side-copy">Latvian company is an ideal instrument for European and International trading. It has all the charachteristics of any European company, but with additional benefits.</p>
    <div class="abs btn-sky feature-btn" style="left:332px">FIND OUT MORE</div>
  </aside>

  <section class="abs hero">
    <div class="abs hero-photo" role="img" aria-label="Businessman on the phone in front of glass office buildings"></div>
    <div class="abs hero-copy">
      <h2>CORVANTEQ</h2>
      <p>IS A TAX ADVISORY FIRM ESTABLISHED BACK IN 2002 IN LIMASSOL, CYPRUS. FOR MORE THAN 10 YEARS</p>
    </div>
    <div class="abs hero-dots"><i></i><i></i><i></i><i></i><i></i></div>
  </section>

  <section class="abs callband">
    <h3>REQUEST A CALL</h3>
    <p>LOREM IPSUM IS SIMPLY DUMMY TEXT OF THE PRINTING AND TYPESETTING INDUSTRY. LOREM IPSUM HAS BEEN THE INDUSTRY'S STANDARD DUMMY TEXT EVER SINCE THE 1500S</p>
    <div class="abs call-btn">Request a call</div>
  </section>

  <main>
    <h3 class="abs side-title about-title">ABOUT CORVANTEQ</h3>
    <div class="abs about-copy">
      <p>Corvanteq is a tax advisory firm established back in 2002 in Limassol, Cyprus. For more than 10 years we are providing tax advisory and company formation services for businesses willing to open new markets, optimize their financial operations and secure private assets.</p>
      <p>We moved our main office to Riga, Latvia in the end of 2011 with the purpose to exploit new opportunities from the fast growing European financial center, as well as to support our existing clients who has already appreciated benefits of using Latvian companies or Bank accounts. We entered into partnership with main Latvian non-residents banks, such as Northvale, Amberline, Rivergate, as well as built our own team of professional lawyers, accountants and tax consultants in order to deliver superior service with competitive prices.</p>
    </div>

    <div class="abs feature-head" style="left:465px;width:351px">TRADING</div>
    <p class="abs feature-copy" style="left:469px">Latvian company is an ideal instrument for European and International trading. It has all the charachteristics of any European company, but with additional benefits - low taxes, ease of set up, cost to registrate and own.</p>
    <div class="abs feature-list" style="left:472px">
      <span><svg width="20" height="10"><rect x="1" y="1" width="18" height="7" fill="none" stroke="#aaa"/></svg>EU VAT NUMBER</span>
      <span><svg width="14" height="12"><rect x="1" y="3" width="12" height="8" fill="#aaa"/></svg>LATVIAN BANK ACCOUNT</span>
      <span><svg width="18" height="14"><ellipse cx="9" cy="4" rx="6" ry="2.5" fill="#aaa"/><ellipse cx="9" cy="9" rx="6" ry="2.5" fill="#aaa"/></svg>CORPORATE TAX 15%</span>
      <span><svg width="14" height="12"><rect x="1" y="1" width="12" height="8" fill="none" stroke="#aaa"/><path d="M4 11h6" stroke="#aaa"/></svg>LATVIAN DOMAIN NAME</span>
      <span><svg width="18" height="14"><path d="M9 2 2 8h2v5h10V8h2z" fill="#aaa"/></svg>LATVIAN LEGAL ADDRESS</span>
      <span><svg width="14" height="14"><path d="M2 2c5 0 10 5 10 10" stroke="#aaa" stroke-width="3" fill="none"/></svg>LATVIAN PHONE NUMBER</span>
    </div>
    <div class="abs btn-sky feature-btn" style="left:704px">FIND OUT MORE</div>

    <div class="abs feature-head" style="left:834px;width:356px;padding-left:21px">HOLDING</div>
    <p class="abs feature-copy" style="left:839px">Latvian company can be used as an International Holding company. Starting from 2013 Latvia introduce favorable regime for international holding, financial companies and companies holding intellectual property.</p>
    <div class="abs feature-list" style="left:843px">
      <span><svg width="20" height="10"><rect x="1" y="1" width="18" height="7" fill="none" stroke="#aaa"/></svg>DIVIDEND TAX 0%</span>
      <span><svg width="14" height="12"><rect x="1" y="3" width="12" height="8" fill="#aaa"/></svg>EU VAT NUMBER</span>
      <span><svg width="18" height="14"><ellipse cx="9" cy="4" rx="6" ry="2.5" fill="#aaa"/><ellipse cx="9" cy="9" rx="6" ry="2.5" fill="#aaa"/></svg>CORPORATE TAX 15%</span>
      <span><svg width="14" height="12"><rect x="1" y="1" width="12" height="8" fill="none" stroke="#aaa"/><path d="M4 11h6" stroke="#aaa"/></svg>CORPORATE TAX 15%</span>
      <span><svg width="18" height="14"><path d="M9 2 2 8h2v5h10V8h2z" fill="#aaa"/></svg>LATVIAN LEGAL ADDRESS</span>
      <span><svg width="14" height="14"><path d="M2 2c5 0 10 5 10 10" stroke="#aaa" stroke-width="3" fill="none"/></svg>LATVIAN LEGAL ADDRESS</span>
    </div>
    <div class="abs btn-sky feature-btn" style="left:1078px">FIND OUT MORE</div>
  </main>

  <footer class="abs footer">
    <div class="footer-links">
      <span>Home</span><i>|</i><span>About us</span><i>|</i><span>About Latvia</span><i>|</i><span>Latvian company</span><i>|</i><span>Our services</span><i>|</i><span>Become Partner</span><i>|</i><span>Corvanteq Travel Guide</span><i>|</i><span>Contacts</span>
    </div>
    <div class="footer-copy">Copyright © 2013. Corvanteq All rights Reserved.</div>
    <div class="social"><i></i><i></i><i></i><i></i></div>
  </footer>

</div>
</body>
</html>
```